Website for Ravok Capital

We need a new web design for a company based in Chicago called "Ravok Capital". Ravok provides portfolio management and financial advice using primarily income oriented strategies, such as, dividend paying stocks and preferred stocks. Our niche is utilizing conservative option strategies to help generate income and minimize risk. We are looking for a clean-cut and streamline professional site that is both appealing and user friendly. We would like the main colors to be the dark blue and bright green of our logo. Depending on cost and ease, we may want a designer to give us the completed website, including the coding, etc.

Target Market(s)

20-80 year old affluent investors seeking portfolio management and investment advice.

Industry/Entity Type

Conservative

Requirements
Must have
• -our logo
-main tabs: home, about us, our philosophy, our services, investment strategy, compliance, contact us
-our phone number visible and conveniently placed on each page
Nice to have
• -conveniently placed login button for current clients
-conveniently placed "quick contact" box on home page with spaces for first name, last name, email, phone number, and a blank box for their question or comment
-check us out on Facebook and Twitter logos/buttons
-we like the idea of rotating pictures on top of page, but we aren't sure whether or not we definitely want that
Should not have
• -no trees
-no clocks
-no timers
-no crowns
-no plants

```html
<!DOCTYPE html>
<html lang="en">
<head>
<meta charset="utf-8">
<title>Ravok Capital</title>
<link href="https://fonts.googleapis.com/css2?family=Source+Sans+3:wght@400;600;700&display=swap" rel="stylesheet">
<style>
:root{
  --navy:#22296b;
  --green:#6ab93c;
  --green-dark:#559a2c;
  --blue:#1d4f96;
  --text:#444;
  --muted:#f2f2f2;
  --line:#d9d9d9;
  --footer:#1c1c1c;
  --footer-bar:#2b2b2b;
}
*{box-sizing:border-box;margin:0;padding:0}
html,body{width:800px;height:1200px;overflow:hidden;background:#fff}
body{position:relative;font-family:"Source Sans 3",sans-serif;color:var(--text)}
.abs{position:absolute}
.brand{display:flex;align-items:center;gap:8px;font-weight:700;color:var(--navy);white-space:nowrap}
.brand .dot{width:14px;height:14px;border-radius:50%;background:var(--green);flex:none}
.header-brand{left:40px;top:20px;font-size:24px}
.topbar{font-size:10.5px;color:#333;display:flex;align-items:center;gap:5px}
.topbar b{font-weight:400;color:var(--navy);font-size:11.5px}
.social{width:16px;height:16px;border-radius:3px;background:#7fa3c9;display:inline-block}
.nav{left:16px;top:82px;width:762px;height:36px;border:2px solid #e4e4e4;background:linear-gradient(#fff,#f3f3f3);display:flex;font-size:12.5px;color:#222;text-transform:uppercase;letter-spacing:-.2px}
.nav span{display:flex;align-items:center;padding:0 16px}
.nav span:first-child{padding-left:24px;padding-right:20px}
.nav .active{background:var(--green);color:#fff;border:1px solid var(--green-dark)}
.hero{left:18px;top:126px;width:760px;height:269px;border:4px solid #e6e6e6;background:#fff;overflow:hidden}
.hero-photo{position:absolute;right:0;top:0;width:420px;height:100%;background:linear-gradient(90deg,#fff 0%,#dfe4ea 25%,#a9b8c9 60%,#4e6f9c 100%)}
.hero-brand{left:30px;top:40px;font-size:30px}
.hero h1{position:absolute;left:36px;top:112px;font-size:16px;font-weight:600;color:var(--green)}
.hero p{position:absolute;left:36px;top:138px;width:310px;font-size:9.5px;line-height:15px;color:#333}
.btn{display:inline-flex;align-items:center;justify-content:center;color:#fff;font-weight:700;text-transform:uppercase;border-radius:3px}
.hero .btn{position:absolute;left:33px;top:189px;width:111px;height:35px;font-size:14px;background:var(--green);letter-spacing:-.2px}
.feature{top:410px;width:236px;height:117px;background:linear-gradient(#f4f4f4,#e8e8e8)}
.feature .art{position:absolute;left:0;top:16px;width:72px;height:86px}
.feature h2{position:absolute;left:84px;top:14px;font-size:12px;font-weight:600;color:var(--blue)}
.feature.green h2{color:var(--green-dark)}
.feature p{position:absolute;left:86px;top:34px;width:144px;font-size:9px;line-height:12px;color:#222;text-align:justify}
.feature .btn{position:absolute;left:86px;top:82px;width:70px;height:26px;font-size:9px;background:var(--green);border:1px solid var(--green-dark)}
.feature .btn.navy{background:var(--blue);border-color:var(--navy)}
.about-title{left:33px;top:561px;font-size:14px;color:#222;white-space:nowrap}
.about-title .n{color:var(--navy);font-weight:600;margin:0 4px 0 8px}
.about-title .g{color:var(--green);font-size:12.5px}
.about-text{left:33px;top:590px;width:471px;font-size:10.4px;line-height:15.2px;text-align:justify}
.about-sub{left:35px;top:703px;font-size:10.5px;color:var(--green-dark)}
.checklist{top:730px;list-style:none;font-size:10.5px;line-height:15.2px;color:var(--navy)}
.checklist li{display:flex;align-items:center;gap:10px}
.checklist svg{width:9px;height:9px}
.qc-title{left:532px;top:561px;font-size:14px;color:#222}
.qc-label{left:534px;font-size:11.5px;color:#444}
.qc-input{left:601px;width:160px;height:28px;border:1px solid var(--line);background:#f7f8f9}
.qc-area{left:536px;top:736px;width:225px;height:77px;border:1px solid var(--line);background:#f7f8f9}
.submit{left:672px;top:823px;width:87px;height:28px;font-size:12px;background:var(--navy);letter-spacing:.4px}
.testi{left:30px;top:866px;width:731px;height:140px;background:#e5e5e5}
.testi h2{position:absolute;left:29px;top:9px;font-size:14px;font-weight:600;color:var(--blue)}
.quote{position:absolute;left:28px;top:37px;width:674px;height:70px;background:#dadada;border:1px solid #cfcfcf}
.quote .photo{position:absolute;left:15px;top:7px;width:61px;height:55px;background:linear-gradient(#8c97a3,#5c5a55)}
.quote p{position:absolute;left:86px;top:7px;width:577px;font-size:9.5px;line-height:15px;color:#555;text-align:justify}
.testi .who{position:absolute;left:594px;top:118px;font-size:11.5px;color:var(--blue)}
.arrow{top:922px;width:32px;height:32px;border-radius:50%;background:#fff;border:1px solid #ddd}
.footer{left:0;top:1029px;width:800px;height:136px;background:var(--footer)}
.footer-col{top:1051px;font-size:9.5px;line-height:15.2px;color:#eee}
.footer-col h3{font-size:11.5px;font-weight:600;color:var(--green);margin-bottom:8px}
.footer-col .hl{color:var(--green)}
.footer-brand{left:612px;top:1086px;font-size:24px;color:#fff}
.footer-brand .dot{background:var(--green)}
.bottom{left:0;top:1165px;width:800px;height:35px;background:var(--footer-bar);color:#eee;font-size:10px;display:flex;align-items:center;justify-content:center;gap:14px}
</style>
</head>
<body>

<div class="abs brand header-brand"><span class="dot"></span>Ravok Capital</div>

<div class="abs topbar" style="left:484px;top:17px">
  <svg width="12" height="12" viewBox="0 0 12 12"><rect width="12" height="12" rx="2" fill="#3f9e45"/><path d="M3.5 3c.8 2.6 2.6 4.6 5 5.5l.9-1.1-1.4-.9-.7.6C6.2 6.5 5.4 5.7 4.9 4.6l.6-.7L4.6 2.5z" fill="#fff"/></svg>
  Call Us : <b>(312) 555-0148</b>
</div>
<div class="abs topbar" style="left:632px;top:17px">
  <svg width="12" height="12" viewBox="0 0 12 12"><circle cx="6" cy="6" r="6" fill="#8cc63f"/><rect x="5.2" y="2.5" width="1.6" height="4.5" fill="#fff"/><rect x="5.2" y="8" width="1.6" height="1.6" fill="#fff"/></svg>
  Client Login
</div>
<div class="abs topbar" style="left:488px;top:44px;gap:8px">
  Share With Us :
  <span class="social"></span><span class="social"></span><span class="social"></span>
</div>

<nav class="abs nav">
  <span>Home</span><span class="active">About Us</span><span>Our Philosophy</span><span>Our Services</span><span>Investment Strategy</span><span>Compliance</span><span>Contact Us</span>
</nav>

<section class="abs hero">
  <div class="hero-photo" role="img" aria-label="Photo of a smiling businessman in a blue shirt and tie at an office desk"></div>
  <div class="abs brand hero-brand"><span class="dot"></span>Ravok Capital</div>
  <h1>EMPOWERING YOU TO DO MORE</h1>
  <p>Curabitur feugiat mattis sapien, pharetra cursus elit lobortis ornare. Ut ultrices cursus nunc eget consectetur. Praesent lectus erat, auctor a tincidunt sed</p>
  <span class="btn">Read More</span>
</section>

<div class="abs feature" style="left:30px">
  <div class="art" role="img" aria-label="Illustration of a computer monitor showing a rising line chart" style="background:linear-gradient(#dfe6ee,#9aa6b3)"></div>
  <h2>FINANCIAL ADVICE</h2>
  <p>Donec sed augue erat. Morbi in justo neque, id porttitor turpis. Cum sociis natoque parturient</p>
  <span class="btn navy">Read More</span>
</div>
<div class="abs feature green" style="left:278px">
  <div class="art" role="img" aria-label="Illustration of a bar chart with a rising green arrow" style="background:linear-gradient(#eef2ec,#9fcf7c)"></div>
  <h2>INVESTMENT STRATEGY</h2>
  <p>Donec sed augue erat. Morbi in justo neque, id porttitor turpis. Cum sociis natoque parturient</p>
  <span class="btn">Read More</span>
</div>
<div class="abs feature green" style="left:526px">
  <div class="art" role="img" aria-label="Illustration of a grey gear with a red screwdriver" style="background:linear-gradient(#e6e6e6,#b9b9b9 60%,#c9403a)"></div>
  <h2>PORTFOLIO MANAGEMENT</h2>
  <p>Donec sed augue erat. Morbi in justo neque, id porttitor turpis. Cum sociis natoque parturient</p>
  <span class="btn">Read More</span>
</div>

<h2 class="abs about-title" style="font-weight:400">LITTLE ABOUT<span class="n">Ravok</span><span class="g">INVESTMENT</span></h2>
<p class="abs about-text">Lorem ipsum dolor sit amet, consectetur adipiscing elit. Pellentesque scelerisque turpis in enim faucibus eleifend. Sed vitae nisi a risus tempor porta. Nulla sit amet sodales dui. Duis sit amet mi magna, eget sagittis eros. Mauris ullamcorper, justo in porttitor vulputate Donec sed augue erat. Morbi in justo neque, id porttitor turpis. Aliquam diam odio, cursus nec molestie at, sollicitudin eu dolor. Vivamus tempus eleifend lorem ut pulvinar. Nulla sit amet sodales dui. Duis sit amet mi magna, eget sagittis eros. Mauris ullamcorper, justo in porttitor vulputate Donec sed augue erat. Morbi in justo neque, id porttitor turpis.</p>
<p class="abs about-sub">We typically offering some type of&nbsp; services are ,</p>

<ul class="abs checklist" style="left:37px">
  <li><svg viewBox="0 0 9 9"><rect x=".5" y="1.5" width="7" height="7" fill="none" stroke="#333"/><path d="M2 4.5l2 2L8.5.5" fill="none" stroke="#333" stroke-width="1.4"/></svg>Nulla sit amet sodales dui</li>
  <li><svg viewBox="0 0 9 9"><rect x=".5" y="1.5" width="7" height="7" fill="none" stroke="#333"/><path d="M2 4.5l2 2L8.5.5" fill="none" stroke="#333" stroke-width="1.4"/></svg>Duis sit amet mi magna</li>
  <li><svg viewBox="0 0 9 9"><rect x=".5" y="1.5" width="7" height="7" fill="none" stroke="#333"/><path d="M2 4.5l2 2L8.5.5" fill="none" stroke="#333" stroke-width="1.4"/></svg>Eget sagittis eros</li>
  <li><svg viewBox="0 0 9 9"><rect x=".5" y="1.5" width="7" height="7" fill="none" stroke="#333"/><path d="M2 4.5l2 2L8.5.5" fill="none" stroke="#333" stroke-width="1.4"/></svg>Mauris ullamcorper</li>
  <li><svg viewBox="0 0 9 9"><rect x=".5" y="1.5" width="7" height="7" fill="none" stroke="#333"/><path d="M2 4.5l2 2L8.5.5" fill="none" stroke="#333" stroke-width="1.4"/></svg>Justo in porttitor vulputate</li>
</ul>
<ul class="abs checklist" style="left:209px">
  <li><svg viewBox="0 0 9 9"><rect x=".5" y="1.5" width="7" height="7" fill="none" stroke="#333"/><path d="M2 4.5l2 2L8.5.5" fill="none" stroke="#333" stroke-width="1.4"/></svg>Nulla sit amet sodales dui</li>
  <li><svg viewBox="0 0 9 9"><rect x=".5" y="1.5" width="7" height="7" fill="none" stroke="#333"/><path d="M2 4.5l2 2L8.5.5" fill="none" stroke="#333" stroke-width="1.4"/></svg>Duis sit amet mi magna</li>
  <li><svg viewBox="0 0 9 9"><rect x=".5" y="1.5" width="7" height="7" fill="none" stroke="#333"/><path d="M2 4.5l2 2L8.5.5" fill="none" stroke="#333" stroke-width="1.4"/></svg>Eget sagittis eros</li>
  <li><svg viewBox="0 0 9 9"><rect x=".5" y="1.5" width="7" height="7" fill="none" stroke="#333"/><path d="M2 4.5l2 2L8.5.5" fill="none" stroke="#333" stroke-width="1.4"/></svg>Mauris ullamcorper</li>
  <li><svg viewBox="0 0 9 9"><rect x=".5" y="1.5" width="7" height="7" fill="none" stroke="#333"/><path d="M2 4.5l2 2L8.5.5" fill="none" stroke="#333" stroke-width="1.4"/></svg>Justo in porttitor vulputate</li>
</ul>

<h2 class="abs qc-title" style="font-weight:400">QUICK CONTACT</h2>
<span class="abs qc-label" style="top:592px">First Name</span>
<div class="abs qc-input" style="top:586px"></div>
<span class="abs qc-label" style="top:631px">Last Name</span>
<div class="abs qc-input" style="top:622px"></div>
<span class="abs qc-label" style="top:667px">Email id</span>
<div class="abs qc-input" style="top:659px"></div>
<span class="abs qc-label" style="top:705px">Phone</span>
<div class="abs qc-input" style="top:696px"></div>
<div class="abs qc-area"></div>
<span class="abs btn submit">Submit</span>

<section class="abs testi">
  <h2>CLIENT TESTIMONIALS</h2>
  <div class="quote">
    <div class="photo" role="img" aria-label="Portrait photo of the client"></div>
    <p>Lorem ipsum dolor sit amet, consectetur adipiscing elit. Pellentesque scelerisque turpis in enim faucibus eleifend. Sed vitae nisi a risus tempor porta. Pellentesque arcu odio, commodo eget malesuada id, interdum non nunc. Curabitur dignissim, diam non tristique consequat, odio est varius ante, sed semper est leo eget dolor.</p>
  </div>
  <span class="who">Daniel Morrow , USA</span>
</section>
<svg class="abs arrow" style="left:19px" viewBox="0 0 32 32"><path d="M19 9l-7 7 7 7" fill="none" stroke="#6ab93c" stroke-width="2.5"/></svg>
<svg class="abs arrow" style="left:742px" viewBox="0 0 32 32"><path d="M13 9l7 7-7 7" fill="none" stroke="#6ab93c" stroke-width="2.5"/></svg>

<footer class="abs footer"></footer>
<div class="abs footer-col" style="left:35px"><h3>OUR SERVICES</h3>Curabitur feugiat<br>mattissa ienphare<br>cursus elit obortis<br>Ornare amron</div>
<div class="abs footer-col" style="left:162px"><h3>USEFUL LINKS</h3>Curabitur feugiat<br>mattissa ienphare<br>cursus elit obortis<br>Ornare amron</div>
<div class="abs footer-col" style="left:286px"><h3>OUR SOLUTIONS</h3>Curabitur feugiat<br>mattissa ienphare<br>cursus elit obortis<br>Ornare amron</div>
<div class="abs footer-col" style="left:421px"><h3>CONTACT US</h3><span style="font-size:10.5px">Lorem ipsum dolor sit amet consrtut</span><br>2210 W Harlow St<br>Chicago, Illinois<br>Phone: <span class="hl">(312) 555-0148</span><br>Fax: <span class="hl">(312) 555-0192</span></div>
<div class="abs brand footer-brand"><span class="dot"></span>Ravok Capital</div>

<div class="abs bottom"><span>Copyright 2013</span><span>|</span><span>All Rights Reserved</span><span>|</span><span>Privacy Policy</span></div>

</body>
</html>
```